Startup company business card (Media & Advertising)

we need a business card design for a company that is a startup in the media and aggregation industry. Card needs to look funky and of a new breed/modern and upmarket.

Target Market(s)

advertisers/ brand agencies & media publishers

Industry/Entity Type

Advertising

Contact Information for Business Card

Please ensure the front face signifies our brand (plintovo.com) and back has details for the contact. Standard contact such as phone , address, email , website etc.

Font styles to use
Other font styles liked:
• use styleguide and logo font and color

Colors

Designer to choose colors to be used in the design.

Requirements
Must have
• We are disrupting the media and agency industry so subtlety would be good to use imagery to signify this
Nice to have
• Please use logo colors for branding
Should not have
• be as creative and provide few options. Pick a brand color from logo and styleguide

```html
<!DOCTYPE html>
<html lang="en">
<head>
<meta charset="utf-8">
<title>plintovo business card</title>
<link rel="stylesheet" href="https://fonts.googleapis.com/css2?family=Arvo:wght@400;700&family=Mulish:wght@400;500&display=swap">
<style>
  :root {
    --backdrop: #c6c6c6;
    --card-light: #f1f1f1;
    --brand-red: #e0323e;
    --brand-wine: #961a3c;
    --ink: #1d1d1d;
    --ink-soft: #444444;
    --rule: #6a6a6a;
    --blush: #efcfc4;
    --white: #ffffff;
  }
  * { box-sizing: border-box; margin: 0; padding: 0; }
  html, body { width: 1200px; height: 1200px; overflow: hidden; }
  body { background: var(--backdrop); position: relative; font-family: "Mulish", sans-serif; }

  .card {
    position: absolute;
    left: 232px;
    width: 736px;
    height: 424px;
    border-radius: 48px;
    overflow: hidden;
  }
  .card--front { top: 106px; background: var(--card-light); }
  .card--back { top: 662px; background: var(--brand-wine); }

  .brand {
    position: absolute;
    display: flex;
    align-items: center;
    gap: 18px;
    font-family: "Arvo", serif;
    font-weight: 700;
    letter-spacing: 0.5px;
  }
  .brand__dot { border-radius: 50%; background: var(--brand-red); flex: none; }

  .card--front .brand { left: 70px; top: 72px; font-size: 46px; color: var(--ink); }
  .card--front .brand__dot { width: 56px; height: 56px; }

  .front-deco {
    position: absolute;
    left: 413px; top: 20px;
    width: 310px; height: 190px;
    border-radius: 60% 40% 50% 50%;
    background: radial-gradient(ellipse at 55% 40%, var(--blush) 0%, rgba(239,207,196,0.5) 55%, rgba(241,241,241,0) 78%);
  }

  .holder { position: absolute; left: 70px; top: 208px; }
  .holder__name { font-family: "Arvo", serif; font-weight: 700; font-size: 24px; color: var(--brand-red); line-height: 1.2; }
  .holder__role { font-size: 17px; color: var(--ink-soft); line-height: 1.3; }

  .divider { position: absolute; left: 70px; top: 271px; width: 595px; height: 1.5px; background: var(--rule); }

  .contacts { position: absolute; left: 70px; top: 292px; list-style: none; }
  .contacts li { display: flex; align-items: center; gap: 10px; font-size: 17px; color: var(--ink-soft); height: 22px; }
  .contacts svg { width: 15px; height: 15px; fill: var(--brand-red); flex: none; }

  .address { position: absolute; right: 71px; top: 314px; text-align: right; font-size: 17px; color: var(--ink-soft); line-height: 22px; }

  .back-map {
    position: absolute;
    left: 52px; top: 54px;
    width: 632px; height: 308px;
    border-radius: 40%;
    background: radial-gradient(ellipse at 50% 45%, rgba(220,80,100,0.35) 0%, rgba(200,60,90,0.18) 50%, rgba(150,26,60,0) 75%);
  }
  .card--back .brand { left: 0; right: 0; top: 168px; justify-content: center; font-size: 52px; color: var(--white); }
  .card--back .brand__dot { width: 70px; height: 70px; }
  .tagline {
    position: absolute; left: 0; right: 0; top: 262px;
    text-align: center;
    font-family: "Arvo", serif; font-weight: 700; font-size: 28px;
    color: var(--white);
  }
</style>
</head>
<body>
  <section class="card card--front">
    <div class="front-deco" role="img" aria-label="Faint large brand decoration"></div>
    <div class="brand"><span class="brand__dot"></span>plintovo</div>
    <div class="holder">
      <p class="holder__name">Daniel Ashworth</p>
      <p class="holder__role">Managing Director</p>
    </div>
    <div class="divider"></div>
    <ul class="contacts">
      <li><svg viewBox="0 0 16 16"><path d="M2 5c0-2 3-3 6-3s6 1 6 3v1h-3V5H5v1H2zM3 8l2-2h6l2 2v5H3zm5 1.5a1.5 1.5 0 1 0 0 3 1.5 1.5 0 0 0 0-3z"/></svg>(+61) 7 5550 0142</li>
      <li><svg viewBox="0 0 16 16"><path d="M1 4h14v8H1zm1.5 1 5.5 4 5.5-4z" fill-rule="evenodd"/></svg>hello@plintovo.com</li>
      <li><svg viewBox="0 0 16 16"><path d="M8 1a7 7 0 1 0 0 14A7 7 0 0 0 8 1zm0 1.5c.9 0 1.9 1.6 2.2 4.5H5.8C6.1 4.1 7.1 2.5 8 2.5zM2.6 7h1.9c.1-1.5.5-2.9 1-3.8A5.5 5.5 0 0 0 2.6 7zm8.9 0h1.9a5.5 5.5 0 0 0-2.9-3.8c.5.9.9 2.3 1 3.8zM2.6 9a5.5 5.5 0 0 0 2.9 3.8c-.5-.9-.9-2.3-1-3.8zm3.2 0c.3 2.9 1.3 4.5 2.2 4.5s1.9-1.6 2.2-4.5zm5.7 0c-.1 1.5-.5 2.9-1 3.8A5.5 5.5 0 0 0 13.4 9z"/></svg>www.plintovo.com</li>
    </ul>
    <p class="address">PO Box 4120 Harlow St<br>Riverton City Country 4120</p>
  </section>

  <section class="card card--back">
    <div class="back-map" role="img" aria-label="Dotted world map"></div>
    <div class="brand"><span class="brand__dot"></span>plintovo</div>
    <p class="tagline">Advertise anywhere, anytime!</p>
  </section>
</body>
</html>
```